INNOVATIVE DESIGN NEEDED FOR FINANCIAL COMPANY

INTERNATIONAL FIRM IN HONG KONG NEEDS A MODERN BUSINESS CARD DESIGN. ONE SIDE ENGLISH OTHER SIDE IN CHINESE. WE ARE OPEN TO CHANGING FONTS AND COLOR. SHOULD BE A CARD THAT IS PROFESSIONAL DEALING WITH HIGH NET WORTH CLIENTELE. BOTH SIDES OF THE CARD WILL BE THE SAME, HOWEVER, THE WORDING ON ONE SIDE WILL BE ENGLISH AND THE OTHER SIDE IN CHINESE (CAN ASSIST IN THE LETTERING - CAN PROVIDE ONCE CARD DESIGN IS ACCEPTED.

Target Market(s)

Hong Kong/CHINA

Contact Information for Business Card

ATTRACTIVE MODERN

```html
<!DOCTYPE html>
<html lang="en">
<head>
<meta charset="utf-8">
<title>Cedarline Asset Management – Business Card</title>
<link rel="stylesheet" href="https://fonts.googleapis.com/css2?family=Noto+Sans+TC:wght@900&family=Archivo+Black&family=Arimo:wght@400;700&display=swap">
<style>
  :root {
    --backdrop: #2b2b2b;
    --card: #ffffff;
    --ink: #2f2f2f;
    --ink-soft: #6a6a6a;
    --brand-green: #138a68;
  }
  * { margin: 0; padding: 0; box-sizing: border-box; }
  html, body { width: 1200px; height: 1189px; overflow: hidden; }
  body {
    background: var(--backdrop);
    display: flex; align-items: center; justify-content: center;
    font-family: "Arimo", Arial, sans-serif;
    color: var(--ink);
  }
  .business-card {
    position: relative;
    width: 1000px; height: 570px;
    background: var(--card);
    border-radius: 34px;
  }
  .company-block { position: absolute; left: 70px; top: 62px; }
  .company-name-zh {
    font-family: "Noto Sans TC", sans-serif;
    font-weight: 900; font-size: 50px; letter-spacing: 2px;
    color: var(--ink); line-height: 1;
  }
  .company-name-en {
    font-family: "Archivo Black", "Arial Black", sans-serif;
    font-size: 20px; letter-spacing: 4.5px;
    color: var(--ink-soft); margin-top: 8px;
  }
  .person-block { position: absolute; left: 78px; top: 218px; }
  .person-name { font-weight: 700; font-size: 36px; line-height: 1; }
  .person-title { font-size: 27px; color: var(--brand-green); margin-top: 4px; }
  .address-block {
    position: absolute; left: 82px; top: 318px;
    font-size: 27px; line-height: 38px; color: var(--ink);
  }
  .contact-list {
    position: absolute; left: 82px; top: 412px;
    list-style: none; font-size: 27px;
  }
  .contact-list li { display: flex; align-items: center; height: 40px; }
  .contact-list svg { width: 26px; height: 26px; margin-right: 24px; flex: none; }
  .accent { color: var(--brand-green); }
  .brand-mark {
    position: absolute; left: 640px; top: 110px; width: 300px;
    display: flex; flex-direction: column; align-items: center; gap: 24px;
  }
  .brand-dot {
    width: 150px; height: 150px; border-radius: 50%;
    background: var(--brand-green);
  }
  .brand-name {
    font-family: "Arimo", Arial, sans-serif;
    font-weight: 700; font-size: 40px; color: var(--brand-green);
  }
</style>
</head>
<body>
  <article class="business-card">
    <header class="company-block">
      <div class="company-name-zh" lang="zh-Hant">雪松資產管理有限公司</div>
      <div class="company-name-en">Cedarline Asset Management Ltd</div>
    </header>

    <section class="person-block">
      <div class="person-name">Daniel Wong</div>
      <div class="person-title">Director</div>
    </section>

    <address class="address-block" style="font-style: normal;">
      PO BOX 456, Harbour Road<br>
      3rd Floor, Kowloon
    </address>

    <ul class="contact-list">
      <li>
        <svg viewBox="0 0 26 26" aria-hidden="true"><rect x="3" y="3" width="20" height="20" fill="none" stroke="var(--brand-green)" stroke-width="3"/></svg>
        (852) 555 0199
      </li>
      <li>
        <svg viewBox="0 0 26 26" aria-hidden="true"><rect x="1" y="5" width="24" height="16" fill="var(--brand-green)"/><path d="M1 5 L13 14 L25 5 M1 21 L10 12 M25 21 L16 12" fill="none" stroke="#fff" stroke-width="1.6"/></svg>
        hello@cedarline.example
      </li>
      <li>
        <svg viewBox="0 0 26 26" aria-hidden="true"><circle cx="13" cy="13" r="11" fill="var(--brand-green)"/><g fill="none" stroke="#fff" stroke-width="1.4"><ellipse cx="13" cy="13" rx="5" ry="11"/><line x1="2" y1="13" x2="24" y2="13"/><line x1="4" y1="8" x2="22" y2="8"/><line x1="4" y1="18" x2="22" y2="18"/></g></svg>
        www.<span class="accent">cedarline</span>.example
      </li>
    </ul>

    <div class="brand-mark">
      <div class="brand-dot"></div>
      <div class="brand-name">Cedarline</div>
    </div>
  </article>
</body>
</html>
```